San Francisco Leading Consulting firm - 47Nova Web Design Project

•Create a Web Design
•Uncoded webpage layout design
•2 Pages Design - Homepage + Interior Page

Task Description
Hello, we're looking for a re-design our current website www.47nova-example.com

we have a sample mockup design @

http://47nova.civicpane-example.org/

This shows the layout that we like and also a sample of 6 pictures that would change based on where you mouse over..

6 pictures HOME design needs to be included.

SMART
THOUGHTFUL
FLEXIBLE
CREATIVE SERVICES
TECHNICAL SERVICES
PARTNERS

sites we like:

http://www.brelmoradvisory-example.com/Home.cfm?id=Home
http://www.pixelquarry-example.com/index.html

Our company can be best described as: 100+ employees, cutting-edge, depandable, innovative, strong, smart.

Our Primary focus is: IT Consulting Services and Creative Design services

47Nova LLC is a consulting firm providing creative design, business and technology solutions to both private and public interests.

Established in 1996, 47Nova is a San Francisco based company providing specialists for a range of business needs including:

Creative Design Services
•Print
•Logo Design
•Website Design
•Illustration

and

Business and Technology solutions

•Application Software and Web Development
•Business Process Re-Design (BPR)
•Business/Systems Analysis and Requirement Documentation
•Mentoring and Training
•Network/Hardware Installation Services
•System Design and Architecture
•Vendor Management
•Teamvault Architecture and Implementation

our sample mockup site:

Reason: Due to holiday season, we're not available to work with designers and finilize our design.  

Thank you very much for submitting your design.

We appreciate your time and creativity.   Since, our office is currently closed for holidays, we will be reviewing it in details next week and will make our decision as soon as possible.

It would be great if you could submit any of your changes by Wed next week, so it would be part of our reviews. 

Please see updated wireframe under attachments:  we have some minor updates to our wireframe that we would like you to update your designs, if possible.  

We also encorouge you not to use our standard wireframe and come up with more unique designs.   Everything would be considered when we review your design.

 

Target Market(s)

Creative services and professional services clients, including government agencies

Industry/Entity Type

Business

Requirements
Must have
• Clean, professional look, easy navigation

```html
<!DOCTYPE html>
<html lang="en">
<head>
<meta charset="utf-8">
<title>47Nova – Home and Internal Page</title>
<link href="https://fonts.googleapis.com/css2?family=Arimo:wght@400;700&family=Gelasio:wght@400&display=swap" rel="stylesheet">
<style>
:root{
  --board:#ffffff;
  --stage:#222a33;
  --stage-edge:#3b4650;
  --page:#ffffff;
  --teal-dark:#2c7f92;
  --teal:#4aa3b3;
  --teal-light:#bfe1e8;
  --blue:#1b6b93;
  --green:#4f9a1c;
  --text:#55595e;
  --muted:#9aa0a6;
  --rule:#e3e6e8;
  --menu:#e9ecee;
  --menu-active:#cfd6db;
  --footer:#e4e6e8;
}
*{box-sizing:border-box;margin:0;padding:0}
html,body{width:1200px;height:900px;overflow:hidden;background:var(--board)}
body{position:relative;font-family:"Arimo",Arial,sans-serif;color:var(--text)}

.stage{position:absolute;background:var(--stage);box-shadow:inset 0 0 0 14px var(--stage-edge)}
.stage--home{left:0;top:0;width:660px;height:660px}
.stage--internal{left:600px;top:236px;width:600px;height:664px}

.board-label{position:absolute;font-family:"Gelasio",Georgia,serif;font-size:34px;color:#111}
.board-label--home{left:208px;top:672px}
.board-label--internal{left:808px;top:172px}

.page{position:absolute;background:var(--page);overflow:hidden}
.page--home{left:76px;top:0;width:504px;height:650px}
.page--internal{left:676px;top:240px;width:474px;height:600px}

.brand{position:absolute;left:14px;top:12px;display:flex;align-items:center;gap:6px;font-size:22px;font-weight:700;color:var(--blue)}
.brand__mark{width:22px;height:22px;background:var(--teal)}
.util-icons{position:absolute;right:40px;top:10px;display:flex;flex-direction:column;gap:7px}
.util-icons span{width:7px;height:7px;border-radius:50%;background:#c9ced2}

.banner{position:absolute;left:0;right:0;background:linear-gradient(100deg,#2d8599 0%,#6cb8c6 45%,#d6ecf1 75%,#a9d2dc 100%)}
.page--home .banner{top:64px;height:126px}
.page--internal .banner{top:56px;height:128px}
.banner__photo{position:absolute;right:30px;top:0;bottom:0;width:120px;background:linear-gradient(180deg,#e8f3f6,#b7d9e1)}
.banner__tagline{position:absolute;left:40px;top:34px;color:#fff;font-size:15px;line-height:1.2}
.banner__tagline strong{display:block;font-size:19px;font-weight:400}
.banner-rule{position:absolute;left:0;right:0;height:4px;background:var(--teal-light)}
.page--home .banner-rule{top:190px}
.page--internal .banner-rule{top:184px}

.col{position:absolute;top:206px;font-size:7.5px;line-height:1.45}
.page--home .col--menu{left:12px;width:150px}
.page--home .col--overview{left:172px;width:150px;border-left:1px solid var(--rule);padding-left:10px;height:350px}
.page--home .col--contracts{left:332px;width:160px;border-left:1px solid var(--rule);padding-left:10px;height:350px}

.heading{display:flex;align-items:center;gap:6px;margin-bottom:10px;font-weight:700;font-size:10px}
.heading__icon{width:26px;height:26px;border-radius:4px}
.heading--blue{color:var(--blue)} .heading--blue .heading__icon{background:linear-gradient(135deg,#5fb0d0,#1b6b93)}
.heading--green{color:var(--green)} .heading--green .heading__icon{background:linear-gradient(135deg,#a6d96a,#4f9a1c)}
.heading--gear .heading__icon{border-radius:50%}

.menu{list-style:none;margin-bottom:34px}
.menu li{background:var(--menu);margin-bottom:2px;padding:3px 8px;font-weight:700;font-size:7px;color:#333}
.menu li.is-active{background:var(--menu-active)}
.menu li::before{content:"";display:inline-block;width:3px;height:3px;background:var(--blue);margin-right:5px;vertical-align:middle}

.sub-link{font-size:6px;color:var(--muted);margin-bottom:6px}
.badge{display:flex;align-items:center;gap:8px;height:42px;margin-bottom:8px;border:1px solid #d9dde0;background:linear-gradient(#fafbfb,#e7eaec);padding-left:8px;font-size:11px;color:var(--muted);line-height:1.05}
.badge__shape{width:26px;height:26px;border-radius:50%;background:#c8ced3}
.badge--support .badge__shape{background:#9fc7d8}
.badge strong{color:var(--teal-dark)}

.copy{text-align:justify;color:var(--text)}
.more{text-align:right;color:var(--green);font-weight:700;font-size:6.5px;margin:4px 0 22px}
.more::before{content:"";display:inline-block;width:5px;height:5px;background:var(--green);margin-right:3px;vertical-align:middle}

.login{margin-top:6px;background:linear-gradient(#2c7f92,#4aa3b3);padding:8px;color:#fff}
.login__title{font-weight:700;font-size:7.5px;margin-bottom:7px}
.login__field{height:13px;background:#fff;border-radius:2px;margin-bottom:6px;font-size:6px;color:var(--muted);padding:2px 5px}
.login__button{display:block;margin-left:auto;width:44px;text-align:center;background:#fff;color:var(--teal-dark);font-size:6px;font-weight:700;padding:2px 0;border-radius:2px}
.forgot{font-size:6px;color:var(--green);text-align:right;margin-top:6px}

.footer{position:absolute;left:10px;right:10px;height:22px;background:var(--footer);font-size:6.5px;color:var(--muted);text-align:right;padding:7px 12px}
.page--home .footer{top:570px}
.page--internal .footer{top:568px}

.page--internal .col--menu{left:12px;width:130px;top:200px}
.page--internal .col--about{left:154px;width:308px;top:200px;border-left:1px solid var(--rule);padding-left:10px;height:350px;font-size:7px;line-height:1.5}
.about-title{font-weight:700;font-size:10px;color:var(--blue);margin-bottom:8px}
.col--about p{margin-bottom:7px}
.col--about ul{list-style:none;margin-bottom:7px}
.col--about li::before{content:"- "}
</style>
</head>
<body>

<div class="stage stage--home"></div>
<div class="stage stage--internal"></div>
<div class="board-label board-label--home">Home</div>
<div class="board-label board-label--internal">Internal page</div>

<!-- Home page -->
<section class="page page--home">
  <div class="brand"><span class="brand__mark"></span>47Nova</div>
  <div class="util-icons"><span></span><span></span><span></span></div>
  <div class="banner" role="img" aria-label="Teal sky with clouds behind the header">
    <div class="banner__photo" role="img" aria-label="Photo of a man working on a laptop"></div>
    <div class="banner__tagline">your<strong>dedicated server</strong><strong>support</strong></div>
  </div>
  <div class="banner-rule"></div>

  <div class="col col--menu">
    <div class="heading heading--blue"><span class="heading__icon" role="img" aria-label="Menu icon"></span>Additional Menu</div>
    <ul class="menu">
      <li class="is-active">Home</li><li>Company</li><li>Technical Services</li><li>Creative Services</li><li>Partners</li><li>Contacts</li>
    </ul>
    <div class="sub-link">Click here to online connect sub link</div>
    <div class="badge badge--support"><span class="badge__shape"></span><div><strong>ONLINE</strong><br>SUPPORT</div></div>
    <div class="badge"><span class="badge__shape"></span><div>OUR <strong>EMAIL</strong><br>CONTACT</div></div>
  </div>

  <div class="col col--overview">
    <div class="heading heading--green"><span class="heading__icon" role="img" aria-label="Company overview icon"></span>Company Overview</div>
    <p class="copy">47Nova's team has expertise in most databases, operating systems, programming languages and platforms currently used by government. We also excel in providing consultants for IT and non-IT services, as well as staff augmentation and placement services.</p>
    <div class="more">Readmore</div>
    <div class="heading heading--green heading--gear"><span class="heading__icon" role="img" aria-label="Gear icon"></span>How it's working?</div>
    <p class="copy">47Nova's team has expertise in most databases, operating systems, programming languages and platforms currently used by government.</p>
    <div class="more">Readmore</div>
  </div>

  <div class="col col--contracts">
    <div class="heading heading--blue"><span class="heading__icon" role="img" aria-label="Business contracts icon"></span>Business Contracts</div>
    <p class="copy">47Nova's team has expertise in most databases, operating systems, programming languages and platforms currently used by government. We also excel in providing consultants for IT and non-IT services, as well as staff augmentation and placement services. 47Nova's team has expertise in most databases, operating systems, programming languages and platforms currently used by government. We also excel in providing consultants.</p>
    <div class="more">Readmore</div>
    <div class="login">
      <div class="login__title">Login Form</div>
      <div class="login__field">User name</div>
      <div class="login__field">Password</div>
      <span class="login__button">Login now</span>
    </div>
    <div class="forgot">Forgot your password?</div>
  </div>

  <div class="footer">Home | Privacy policy | Contact</div>
</section>

<!-- Internal page -->
<section class="page page--internal">
  <div class="brand"><span class="brand__mark"></span>47Nova</div>
  <div class="util-icons"><span></span><span></span><span></span></div>
  <div class="banner" role="img" aria-label="Teal sky with clouds behind the header">
    <div class="banner__photo" role="img" aria-label="Photo of a man working on a laptop"></div>
    <div class="banner__tagline">your<strong>dedicated server</strong><strong>support</strong></div>
  </div>
  <div class="banner-rule"></div>

  <div class="col col--menu">
    <div class="heading heading--blue"><span class="heading__icon" role="img" aria-label="Menu icon"></span>Additional Menu</div>
    <ul class="menu">
      <li class="is-active">Home</li><li>Company</li><li>Technical Services</li><li>Creative Services</li><li>Partners</li><li>Contacts</li>
    </ul>
    <div class="sub-link">Click here to online connect sub link</div>
    <div class="badge badge--support"><span class="badge__shape"></span><div><strong>ONLINE</strong><br>SUPPORT</div></div>
    <div class="badge"><span class="badge__shape"></span><div>OUR <strong>EMAIL</strong><br>CONTACT</div></div>
  </div>

  <div class="col col--about">
    <div class="about-title">About us</div>
    <p>Our company can be best described as: 100+ employees, cutting-edge, dependable, innovative, strong, smart.</p>
    <p>Our Primary focus is: IT Consulting Services and Creative Design services</p>
    <p>47Nova LLC is a consulting firm providing creative design, business and technology solutions to both private and public interests.</p>
    <p>Established in 1996, 47Nova is a San Francisco based company providing specialists for a range of business needs including:</p>
    <p>Creative Design Services</p>
    <ul><li>Print</li><li>Logo Design</li><li>Website Design</li><li>Illustration</li></ul>
    <p>and</p>
    <p>Business and Technology solutions</p>
    <ul>
      <li>Application Software and Web Development</li>
      <li>Business Process Re-Design (BPR)</li>
      <li>Business/Systems Analysis and Requirement Documentation</li>
      <li>Mentoring and Training</li>
      <li>Network/Hardware Installation Services</li>
      <li>System Design and Architecture</li>
      <li>Vendor Management</li>
      <li>Teamvault Architecture and Implementation</li>
    </ul>
  </div>

  <div class="footer">Home | Privacy policy | Contact</div>
</section>

</body>
</html>
```